UK Finance Lead Generation Website Design

We need a new design, logo and coding for our website SpotBrightRates.com.

Our site uses Pay Per Click traffic in order to generate Life Insurance, Private Medical Insurance, Mortgage & Income Protection leads for PRB regulated brokers from the UK.

So we are looking for a homepage design, landing page/quote page design, thank-you page/privacy/t&c/faq page designs (these will all look very similar as they are just blocks of text).

We are open to all kinds of homepage designs. A good example of a homepage we like is - http://www.pricebazaarly.com. It essentially is a header, CTAs leading to quoting pages for different products, some text block space and footer.

We however have strict requirements for the landing page/quoting pages for the products. Attached are two wireframes for the Life Insurance Landing Page/Quoting page. The most important thing about the landing page design is for it to be a 2 step process. User completes some dropdown and/or radio buttons on step 1, clicks next step and the form changes a longer one asking for personal details (name, email, phone, address etc) with text on the left saying "Congratulations, we've found few quotes for you, just complete our form etc."
The site that we've got that idea from is here - http://www.cover-bench-hub.co.uk/norvale/. Please have in mind we don't like their design, it is just the layout that inspired us.
Here is also a link to our current Life Insurance Landing Page/Quote Page - http://spotbrightrates.com/life-insurance/norvale.php. It also uses 2 step process however it looks ugly, cluttered and does not convert good for us. From our current landing page you can get the fields the form should ask on step 1 and on step 2.

Any color scheme can be used.

For text/copy please use text from http://www.cover-bench-hub.co.uk/norvale/.

An overview of what we need from this project:
- Logo - the name in the logo should be SpotBrightRates
- Homepage design
- Landing page/quoting page design - focus on designing a good Life Insurance Landing Page/Quoting page and with slight variations this page will be adjusted for Private Medical Insurance, Income Protection & Mortgages
- About us/Privacy/T&C/FAQs/Thank-you page design - one design/layout will satisfy all that is needed for these pages.
- Coding of everything (HTML, CSS, JAVASCRIPT) + form validation (we will provide the syntax/rules for the form validation) + tooltips on form fields (as in the provided example http://www.cover-bench-hub.co.uk/norvale/)

What is most important for us:
- Getting a landing page/quoting page design that converts!

18-60 UK Males & Females looking for financial quotes

SpotBrightRates

• 2 Step form for Landing Page/Quoting Page
• Modern & clean design.
• Responsive layout/mobile layout

```html
<!DOCTYPE html>
<html lang="en">
<head>
<meta charset="utf-8">
<title>SpotBrightRates – Norvale Life Insurance Quotes</title>
<link href="https://fonts.googleapis.com/css2?family=Roboto:wght@300;400;500;700&display=swap" rel="stylesheet">
<style>
:root{
  --green:#2e8b2e;
  --green-dark:#1f6e24;
  --green-light:#4caf3a;
  --blue:#2a7ccf;
  --blue-dark:#1b5fa5;
  --ink:#333;
  --ink-soft:#555;
  --muted:#888;
  --panel:#f0f0f0;
  --line:#d6d6d6;
  --white:#fff;
  --footer:#3f3b35;
}
*{margin:0;padding:0;box-sizing:border-box}
html,body{width:700px;height:1200px;overflow:hidden}
body{position:relative;background:var(--white);font-family:'Roboto',Arial,sans-serif;color:var(--ink)}
.abs{position:absolute}

/* hero */
.hero-photo{left:0;top:0;width:700px;height:344px;
  background:linear-gradient(180deg,#6fa6df 0%,#a9cdeb 38%,#d7e3c8 55%,#8aa34c 72%,#6b7d2e 100%)}
.header{left:50px;top:0;width:599px;height:74px;background:var(--white);box-shadow:0 2px 6px rgba(0,0,0,.2)}
.brand{left:22px;top:24px;display:flex;align-items:center;gap:7px}
.brand-mark{width:25px;height:25px;background:var(--green-light);border-radius:3px}
.brand-name{font-weight:700;font-size:16px;color:#222;letter-spacing:.3px}
.phone{right:19px;top:9px;display:flex;align-items:center;gap:6px;font-size:17px;color:#333}
.hours{right:19px;top:32px;font-size:7.5px;color:#333}
.top-nav{right:19px;top:48px;font-size:8.5px;color:#333}
.top-nav .on{color:var(--green-light)}

.quote-box{left:187px;top:94px;width:462px;height:218px;background:var(--white)}
.intro{left:0;top:0;width:197px;height:218px;background:var(--panel)}
.intro h1{position:absolute;left:0;top:20px;width:197px;text-align:center;font-weight:400;font-size:12.5px;color:#222}
.intro h1 span{color:var(--green)}
.insurer-name{position:absolute;left:0;top:80px;width:197px;text-align:center;font-size:22px;font-weight:700;color:#1d3a8a;letter-spacing:1px}
.perks{position:absolute;left:27px;top:128px;list-style:none;font-size:7.5px;color:#333}
.perks li{margin-bottom:11px}
.perks li::before{content:"» ";color:var(--green);font-weight:700}

.form{left:211px;top:19px;width:232px;height:188px;background:var(--white);border:1px solid #ccc;box-shadow:0 1px 4px rgba(0,0,0,.15)}
.form-head{height:31px;background:linear-gradient(var(--green-light),var(--green));color:var(--white);font-size:11.5px;text-align:center;line-height:31px}
.field{position:absolute;left:16px;display:flex;align-items:center;font-size:7.5px;color:#333}
.field label{width:78px}
.field .input{width:125px;height:19px;border:1px solid #bbb;box-shadow:inset 0 1px 2px rgba(0,0,0,.1)}
.radio{display:inline-block;width:8px;height:8px;border:1px solid #999;border-radius:50%;margin-right:5px;vertical-align:middle;position:relative}
.radio.checked::after{content:"";position:absolute;left:1.5px;top:1.5px;width:3px;height:3px;border-radius:50%;background:#333}
.opt{margin-right:10px}
.btn-quote{position:absolute;left:16px;top:152px;width:88px;height:25px;background:linear-gradient(var(--blue),var(--blue-dark));border-radius:2px;color:var(--white);font-size:7.5px;font-weight:500;display:flex;align-items:center;justify-content:space-between;padding:0 7px 0 12px}
.btn-quote i{width:11px;height:11px;border-radius:50%;background:rgba(255,255,255,.25);display:flex;align-items:center;justify-content:center}
.secure{position:absolute;left:113px;top:160px;font-size:5.5px;color:#444;display:flex;align-items:center;gap:3px}

/* partners */
.partners{left:48px;top:412px;width:600px;height:42px;background:#f2f2f2;display:flex;align-items:center;justify-content:space-around;font-size:8px;font-weight:700;color:#555}

/* steps */
.step{top:481px;width:192px;height:198px;background:radial-gradient(circle at 50% 45%,#fff 0%,#ececec 100%);border:1px solid #ccc;box-shadow:0 1px 3px rgba(0,0,0,.15);text-align:center}
.badge{position:absolute;left:49px;top:16px;width:94px;height:94px;border-radius:50%;background:var(--green-dark);border:3px solid var(--white);box-shadow:0 0 0 1px #ccc;color:var(--white);font-size:14px;font-weight:500}
.badge svg{display:block;margin:20px auto 6px}
.step h3{position:absolute;left:0;top:124px;width:100%;font-weight:400;font-size:12px;color:var(--green)}
.step p{position:absolute;left:0;top:144px;width:100%;font-weight:300;font-size:11px;line-height:16px;color:#333}

.claim{left:0;top:704px;width:700px;text-align:center;font-size:17.5px;font-weight:300;color:#444;line-height:24px}
.claim span{color:var(--green)}

/* testimonials */
.review{top:778px;width:192px;height:164px;background:#eee;border:1px solid #d4d4d4;box-shadow:0 1px 3px rgba(0,0,0,.12);text-align:center}
.review h4{margin:20px 16px 0;font-weight:400;font-size:9.5px;line-height:13px;color:var(--green)}
.review p{margin:8px 16px 0;font-size:5.6px;line-height:11px;color:#444}
.author{position:absolute;left:42px;top:111px;display:flex;align-items:center;gap:8px;text-align:left}
.avatar{width:36px;height:36px;border-radius:50%;background:linear-gradient(#c9b8a4,#8b7560);border:2px solid var(--white);box-shadow:0 0 0 1px #ccc}
.author b{display:block;font-weight:500;font-size:7px;color:#333}
.author em{font-size:7px;color:var(--green)}

/* banner */
.banner{left:0;top:964px;width:700px;height:176px;background:linear-gradient(100deg,#7f8a6d 0%,#9aa58a 35%,#c0a98d 62%,#6d7b4a 100%)}
.banner h2{position:absolute;left:60px;top:38px;font-size:14px;font-weight:500;line-height:19px;color:var(--white);text-shadow:0 1px 3px rgba(0,0,0,.5)}
.banner-cta{position:absolute;left:60px;top:112px;width:154px;height:33px;background:linear-gradient(#fafafa,#dcdcdc);border-radius:2px;box-shadow:0 1px 3px rgba(0,0,0,.3);font-size:10px;color:#333;text-align:center;line-height:33px}

.footer{left:0;top:1140px;width:700px;height:60px;background:var(--footer);color:var(--white);text-align:center}
.footer nav{padding-top:16px;font-size:7.5px}
.footer small{display:block;margin-top:12px;font-size:7.5px}
</style>
</head>
<body>

<div class="abs hero-photo" role="img" aria-label="Photo of a smiling woman and man standing in a sunny summer meadow"></div>

<header class="abs header">
  <div class="abs brand"><span class="brand-mark"></span><span class="brand-name">SPOTBRIGHTRATES</span></div>
  <div class="abs phone">
    <svg width="14" height="14" viewBox="0 0 24 24"><circle cx="12" cy="12" r="11" fill="none" stroke="#4caf3a" stroke-width="2"/><path d="M8 6.5l2 .2 1 2.6-1.3 1a7 7 0 0 0 3.9 3.9l1-1.3 2.6 1 .2 2a1.5 1.5 0 0 1-1.5 1.4A10 10 0 0 1 6.6 8 1.5 1.5 0 0 1 8 6.5z" fill="#4caf3a"/></svg>
    0800 246 7180
  </div>
  <div class="abs hours">Mon-Thurs 9:30am-8pm | Fri 9:30am-6pm</div>
  <nav class="abs top-nav"><span class="on">Free Quote</span> &nbsp;|&nbsp; Critical Illness &nbsp;|&nbsp; Over 50s &nbsp;|&nbsp; Mortgage Protection</nav>
</header>

<section class="abs quote-box">
  <div class="abs intro">
    <h1>Find a <span>Great Quote</span> Today!</h1>
    <div class="insurer-name">NORVALE</div>
    <ul class="perks">
      <li>£150,000 of cover from just £5 a month</li>
      <li>Compare all the leading UK insurers</li>
      <li>Cheaper than going direct to the insurer</li>
      <li>Fast, free and no obligation comparison</li>
    </ul>
  </div>
  <div class="abs form">
    <div class="form-head">Get A Free Quote Now</div>
    <div class="field" style="top:45px"><label>Type of Insurance</label><span class="input"></span></div>
    <div class="field" style="top:70px"><label>Cover Period</label><span class="input"></span></div>
    <div class="field" style="top:95px"><label>Amount of cover</label><span class="input"></span></div>
    <div class="field" style="top:127px"><label>Cover required for</label>
      <span class="opt"><span class="radio checked"></span>You</span>
      <span class="opt"><span class="radio"></span>You &amp; Your Partner</span>
    </div>
    <div class="btn-quote">GET A QUOTE <i><svg width="5" height="6" viewBox="0 0 5 6"><path d="M1 .5L4 3 1 5.5" fill="none" stroke="#fff" stroke-width="1.2"/></svg></i></div>
    <div class="secure"><svg width="6" height="8" viewBox="0 0 6 8"><rect x=".5" y="3.5" width="5" height="4" fill="none" stroke="#777"/><path d="M1.5 3.5V2a1.5 1.5 0 0 1 3 0v1.5" fill="none" stroke="#777"/></svg>Safe | Secure | Privacy Protected</div>
  </div>
</section>

<div class="abs partners">
  <span>NORVALE</span><span>VANTOR</span><span>KELMORA</span><span>OSTREL</span><span>PALEWAY</span><span>ALDER MUTUAL</span><span>HOLLIN &amp; REEVE</span><span>MERSEYVALE</span><span>CASTELLAN</span><span>BRENLOW</span>
</div>

<section class="abs step" style="left:49px">
  <div class="badge"><svg width="22" height="24" viewBox="0 0 22 24"><path d="M3 1h11l5 5v17H3z" fill="none" stroke="#fff" stroke-width="1.6"/><path d="M7 11h8M7 15h8M7 19h8" stroke="#fff" stroke-width="1.6"/></svg>Apply</div>
  <h3>STEP 1</h3><p>Fill in our form or<br>call 0800 246 7180</p>
</section>
<section class="abs step" style="left:254px">
  <div class="badge"><svg width="24" height="24" viewBox="0 0 24 24"><path d="M2 7h9v15H2z M11 7l-4-5h7l4 5" fill="none" stroke="#fff" stroke-width="1.6"/><path d="M13 4h9v15h-11" fill="none" stroke="#fff" stroke-width="1.6"/></svg>Compare</div>
  <h3>STEP 2</h3><p>We compare 100s of<br>life insurance plans</p>
</section>
<section class="abs step" style="left:457px">
  <div class="badge"><svg width="22" height="22" viewBox="0 0 22 22"><path d="M1 1h16l4 4v16H1z" fill="none" stroke="#fff" stroke-width="1.6"/><path d="M5 1v6h10V1M5 21v-8h12v8" fill="none" stroke="#fff" stroke-width="1.6"/></svg>Save</div>
  <h3>STEP 3</h3><p>You get a free quote<br>saving up to 45%</p>
</section>

<p class="abs claim">Over <span>40,000 people</span> have used our website<br>to save money on life insurance.</p>

<article class="abs review" style="left:49px">
  <h4>Fantastic service. Friendly<br>and professional.</h4>
  <p>Really helpful company with an excellent service from start to finish. Everything was easy, simple and stress free. And to top it all off, the quote I received was much better than what I had found elsewhere. Will be recommending to friends and family.</p>
  <div class="author"><span class="avatar" role="img" aria-label="Customer portrait"></span><div><b>OWEN HARTLEY</b><em>Marketing Executive</em></div></div>
</article>
<article class="abs review" style="left:254px">
  <h4>Massive savings. This is a true<br>comparison site.</h4>
  <p>Really helpful company with an excellent service from start to finish. Everything was easy, simple and stress free. And to top it all off, the quote I received was much better than what I had found elsewhere. Will be recommending to friends and family.</p>
  <div class="author"><span class="avatar" role="img" aria-label="Customer portrait"></span><div><b>OWEN HARTLEY</b><em>Marketing Executive</em></div></div>
</article>
<article class="abs review" style="left:457px">
  <h4>The advisor I spoke to was pleasant<br>and informative</h4>
  <p>Really helpful company with an excellent service from start to finish. Everything was easy, simple and stress free. And to top it all off, the quote I received was much better than what I had found elsewhere. Will be recommending to friends and family.</p>
  <div class="author"><span class="avatar" role="img" aria-label="Customer portrait"></span><div><b>OWEN HARTLEY</b><em>Marketing Executive</em></div></div>
</article>

<section class="abs banner" role="img" aria-label="Photo of a laughing couple outside their family home">
  <h2>Be safe in the knowledge that your loved ones<br>will be ok if &nbsp;the worst were to happen.<br>Don't leave it to chance.</h2>
  <div class="banner-cta">GET A FREE QUOTE NOW</div>
</section>

<footer class="abs footer">
  <nav>Home &nbsp;|&nbsp; About Us &nbsp;|&nbsp; Blog &nbsp;|&nbsp; Why Choose Us? &nbsp;|&nbsp; FAQs &nbsp;|&nbsp; Contact Us &nbsp;|&nbsp; Sitemap &nbsp;|&nbsp; Privacy Policy &nbsp;|&nbsp; Terms &amp; Conditions</nav>
  <small>Copyright © 2015 Spot Bright Rates. All rights reserved</small>
</footer>

</body>
</html>
```